One of Australia's fastest growing Financial Company looking for an updated business card design!

Meridale Partners Australia is looking for an updated design for our business cards. We would like to keep up our professional appearances and have get new exciting design that fits our company.

The Meridale aim is to facilitate and assist clients in every financial requirement that may arise in financial areas.

We would to see the design to use colour blue and we like the clouds in the background. We have attached two designs we have use before but we need something with more professional and easy to read design.

We would like the website in the back of the card; the employees name more central and stands out; only a postal address; a list of all our locations along the bottom (Ashvale, Corrington, Braxley, Tallowport)

Looking forward to seeing the designs come in!

Target Market(s)

Other Industry Professionals
Middle Class Families

Industry/Entity Type

Finance

Contact Information for Business Card

Name; Company Role; Office Number; Mobile Number; Email Address; Website; Postal Address; Locations

Font styles to use
Serif
Sans Serif

Colors
0492cd
33a6d7
85cae6
85acd3
3176b5
0455a3
cee9f5
d5e2ee

Requirements
Must have
• Name; Company Role; Office Number; Mobile Number; Email Address; Website; Postal Address; Locations
Nice to have
• The colour blue, clouds on the background

```html
<!DOCTYPE html>
<html lang="en">
<head>
<meta charset="utf-8">
<title>Meridale Partners Australia – Business Card</title>
<link href="https://fonts.googleapis.com/css2?family=Exo+2:wght@400;500;600&display=swap" rel="stylesheet">
<style>
  :root {
    --page-bg: #9c9c9c;
    --card-blue: #0492cd;
    --card-blue-light: #33a6d7;
    --card-blue-deep: #0a80bd;
    --cloud-tone: #85cae6;
    --cloud-soft: #85acd3;
    --ink-white: #ffffff;
    --accent-red: #e8322e;
  }
  * { margin: 0; padding: 0; box-sizing: border-box; }
  html, body {
    width: 1200px; height: 800px; overflow: hidden;
    background: var(--page-bg);
    font-family: "Exo 2", "Trebuchet MS", sans-serif;
  }
  .sheet { position: relative; width: 1200px; height: 800px; }
  .card {
    position: absolute;
    width: 560px; height: 320px;
    border-radius: 4px;
    overflow: hidden;
    background: linear-gradient(135deg, var(--card-blue-light) 0%, var(--card-blue) 55%, var(--card-blue-deep) 100%);
    box-shadow: 0 10px 24px rgba(0,0,0,0.25);
    color: var(--ink-white);
  }
  .card--back { left: 80px; top: 60px; }
  .card--front { left: 560px; top: 420px; }

  /* back side */
  .cloud-band {
    position: absolute; left: 0; top: 0; width: 100%; height: 140px;
    background: linear-gradient(180deg, var(--cloud-soft) 0%, var(--cloud-tone) 45%, rgba(133,202,230,0) 100%);
    opacity: 0.75;
  }
  .back-brand {
    position: absolute; left: 0; right: 0; top: 130px;
    display: flex; align-items: center; justify-content: center; gap: 14px;
  }
  .brand-dot {
    width: 22px; height: 22px; border-radius: 50%;
    background: var(--ink-white);
  }
  .brand-name { font-weight: 500; font-size: 64px; letter-spacing: 1px; line-height: 1; }
  .website {
    position: absolute; left: 0; right: 0; top: 226px;
    text-align: center;
    color: var(--accent-red);
    font-size: 17px; font-weight: 500; letter-spacing: 0.5px;
  }

  /* front side */
  .front-brand {
    position: absolute; left: 40px; top: 118px;
    font-size: 44px; font-weight: 500; line-height: 1;
  }
  .contact {
    position: absolute; right: 32px; top: 36px;
    text-align: right;
  }
  .contact-name { font-size: 28px; font-weight: 500; letter-spacing: 0.5px; line-height: 1; }
  .contact-role { font-size: 15px; margin-top: 3px; margin-bottom: 14px; }
  .contact-line {
    display: flex; justify-content: flex-end; align-items: center; gap: 10px;
    font-size: 17px; line-height: 1; margin-bottom: 10px;
  }
  .contact-line svg { width: 15px; height: 15px; flex: none; fill: var(--ink-white); }
  .contact-address { font-size: 17px; line-height: 1.3; margin-top: 2px; padding-right: 25px; }
</style>
</head>
<body>
<main class="sheet">

  <section class="card card--back" aria-label="Card back">
    <div class="cloud-band" role="img" aria-label="Soft clouds across the sky"></div>
    <div class="back-brand">
      <span class="brand-dot"></span>
      <span class="brand-name">Meridale</span>
    </div>
    <p class="website">www.meridalepartnersgroup.com.au</p>
  </section>

  <section class="card card--front" aria-label="Card front">
    <div class="front-brand">Meridale</div>
    <div class="contact">
      <p class="contact-name">HANNAH LOWELL</p>
      <p class="contact-role">Investment Consultant</p>
      <p class="contact-line">(02) 6140
        <svg viewBox="0 0 16 16"><path d="M3 1h3l1.5 3.5-2 1.3a9 9 0 0 0 4.7 4.7l1.3-2L15 10v3a2 2 0 0 1-2 2A12 12 0 0 1 1 3a2 2 0 0 1 2-2z"/></svg>
      </p>
      <p class="contact-line">(04) 512 318 207
        <svg viewBox="0 0 16 16"><path d="M4 0h8a1 1 0 0 1 1 1v14a1 1 0 0 1-1 1H4a1 1 0 0 1-1-1V1a1 1 0 0 1 1-1zm1 2v10h6V2zm3 11a1 1 0 1 0 0 2 1 1 0 0 0 0-2z"/></svg>
      </p>
      <p class="contact-line">meridalepartnersgroup.com.au
        <svg viewBox="0 0 16 16"><path d="M1 3h14v10H1zm1.5 1.2V12h11V4.2L8 8.6z M2.8 4 8 7.6 13.2 4z"/></svg>
      </p>
      <p class="contact-line">Kingsford Post Shop PO BOX 3180
        <svg viewBox="0 0 16 16"><path d="M8 0a5.5 5.5 0 0 1 5.5 5.5C13.5 10 8 16 8 16S2.5 10 2.5 5.5A5.5 5.5 0 0 1 8 0zm0 3.3a2.2 2.2 0 1 0 0 4.4 2.2 2.2 0 0 0 0-4.4z"/></svg>
      </p>
      <p class="contact-address">(Ashvale, Corrington, Braxley, Tallowport)</p>
    </div>
  </section>

</main>
</body>
</html>
```